Print design needed to improve the layout and look of some existing documents

We need someone to take a couple of existing documents that we have and make them look much better using our existing logo and corporate colors etc. We require these to be delivered in a format that will allow our staff to edit the content as necessary via Microsoft word for conversion once finalized into a PDF. Ideally, we will also be able to use this as a newsletter template or for other documents that might be required in our business. www.larchfieldcapital.com.au
Updates

Project Deadline Extended Reason: So far, I have only seen one design that I believe is quite good quality. Added Sunday, July 3, 2016

Target Market(s)

Business owners, executives, retirees

Industry/Entity Type

Financial Service

Font styles to use
Serif

Requirements
Must have
• Design that uses our existing branding and colors. It also needs to be ina form that we can edit the content / update easily. Ideally the format / layout could also be used for other documents such as short newsletters etc.
Nice to have
• Fresh, simple and crisp. Very professional looking.
Should not have
• strange fonts, weird layouts.

```html
<!DOCTYPE html>
<html lang="en">
<head>
<meta charset="utf-8">
<title>Larchfield Capital – Privacy Policy</title>
<link href="https://fonts.googleapis.com/css2?family=Cinzel:wght@700&family=Questrial&family=Mulish:wght@800&display=swap" rel="stylesheet">
<style>
:root{
  --ink:#3b3b3b;
  --body:#4d4d4d;
  --link:#1aa0dc;
  --green:#6cb33f;
  --teal:#2aa79b;
  --blue:#0f9bd7;
  --frame:#e6efec;
  --paper:#ffffff;
}
*{margin:0;padding:0;box-sizing:border-box}
html,body{width:848px;height:1200px;overflow:hidden}
body{background:linear-gradient(135deg,#edf3e6 0%,#e3eef0 50%,#e4edf2 100%);position:relative;font-family:"Questrial",sans-serif;color:var(--body)}
.page{position:absolute;left:20px;top:20px;width:812px;height:1167px;background:var(--paper)}
.brand{position:absolute;left:28px;top:34px;display:flex;align-items:center;gap:8px;font-family:"Questrial",sans-serif;font-size:22px;letter-spacing:1px;color:#5a5a5a}
.brand-mark{width:12px;height:12px;background:var(--teal)}
.heading{position:absolute;font-family:"Cinzel",serif;font-weight:700;color:var(--ink);font-size:21px;line-height:25.5px;letter-spacing:1.2px}
.heading.wide{text-align:justify;text-align-last:justify}
.rule{position:absolute;height:6px}
.rule.gb{background:linear-gradient(90deg,var(--green),var(--teal) 60%,var(--blue))}
.rule.bg{background:linear-gradient(90deg,var(--blue),var(--teal) 40%,var(--green))}
.copy{position:absolute;font-size:15.6px;line-height:20.4px;text-align:justify;hyphens:manual}
.copy a{color:var(--link);text-decoration:none}
.left{left:45px;width:362px}
.right{left:446px;width:362px}
.footer-title{position:absolute;left:45px;top:1068px;font-family:"Mulish",sans-serif;font-weight:800;font-size:22px;color:var(--ink)}
.footer-copy{position:absolute;left:45px;top:1094px;width:640px;font-size:19.5px;line-height:23.6px;color:var(--body)}
.footer-copy a{color:var(--link);text-decoration:none}
</style>
</head>
<body>
<div class="page"></div>

<div class="brand"><span class="brand-mark"></span>Larchfield Capital</div>

<h2 class="heading wide left" style="top:126px;width:290px">Will we disclose<br>the information we<br><span style="display:block;text-align:left;text-align-last:left">collect to anyone?</span></h2>
<div class="rule gb" style="left:3px;top:210px;width:405px"></div>
<p class="copy left" style="top:236px">We do not sell, trade, or rent your personal infor&shy;mation to others. We may disclose your information to third party organisations where you have request that we liaise with or refer you to the organisations. This may include firms providing investment, superannuation, account&shy;ing legal, credit, transactional banking or insur&shy;ance services and may need to provide your information to contractors who supply services to us or to other companies in the event of a corporate sale, merger, reorganisation, dissolu&shy;tion or similar event. However, we will take all reasonable steps to ensure that they protect your information in the same way that we do.</p>
<p class="copy left" style="top:543px">We may also provide your information to others if we are required to do so by law or under some unusual other circumstances which the Privacy Act permits. We will not provide your informa&shy;tion to any overseas recipients unless we are required to by Law.</p>

<h2 class="heading wide left" style="top:722px;width:320px">How can you check,<br>update or change the<br>information we are<br><span style="display:block;text-align:left;text-align-last:left">holding?</span></h2>
<div class="rule gb" style="left:3px;top:831px;width:405px"></div>
<p class="copy left" style="top:862px">Upon receipt of your written request and enough information to allow us to identify the information, we will disclose to you the personal information we hold about you. We will also correct, amend or delete any personal informa&shy;tion that we agree is inaccurate, irrelevant, out of date or incomplete.</p>

<p class="copy right" style="top:128px">In some limited cases, we may need to refuse access to your information or refuse a request for correction. We will advise you as soon as possible after your request if this is the case and the reasons for our refusal.</p>
<p class="copy right" style="top:250px">If you wish to access or correct your personal information please contact our office (see contact details below). We do not charge for receiving a request for access to personal infor&shy;mation or for complying with a correction request.</p>

<h2 class="heading right" style="top:461px;width:300px">What happens if you<br>want to complain?</h2>
<div class="rule gb" style="left:439px;top:521px;width:409px"></div>
<p class="copy right" style="top:549px">If you have any concerns about whether we have complied with the Privacy Act or this Privacy Policy when collecting of handling your personal information, you can call us on 08 6400 2718 or email your concerns to <a href="mailto:admin@larchfieldcapital.com.au">admin@larch&shy;fieldcapital.com.au</a>.</p>
<p class="copy right" style="top:692px">We will consider any privacy related complaint through our internal complaints resolution process and we will try to respond with a decision within 45 days of you making the com-</p>

<h2 class="heading right" style="top:860px;width:300px">Your consent</h2>
<div class="rule bg" style="left:447px;top:895px;width:401px"></div>
<p class="copy right" style="top:923px">By asking us to assist with your financial needs, you consent to the collection and use of the information you have provided to us for the purposes described above.</p>

<h3 class="footer-title">Tell us what you think</h3>
<p class="footer-copy">We welcome your questions and comments about privacy. If you have any concerns or complaints, please contact us on 08 6400 2718 or via email on <a href="mailto:admin@larchfieldcapital.com.au">admin@larchfieldcapital.com.au</a>.</p>
</body>
</html>
```